Vintage label design for Electrical company (stickers)

I'm after a vintage label design for my electrical company, currently trying to break into the upper market in the electrical field so I need something that stands out and is easy to read.
These will be getting made into stickers roughly 90-110mm x 40-60mm with a custom rectangular shape.
The stickers should have

Target Market(s)

Upper electrical market

Industry/Entity Type

Electrical

Font styles to use
Serif
Decorative
Script

Colors
acd037
9ccb3b
33b8a4

Requirements
Must have
• Be unique, edgy, vintage/retro and easy to read. An electrical theme
• Company logo (picture provided below obviously a lime)
• Fern Voltworks
• 0428915043
• Fernvoltworks.com
• Facebook symbol
• as these are going to be stickers I would like my contact details on them
Nice to have
• Same shades of green, fit between 90-110mm x 40-60mm

```html
<!DOCTYPE html>
<html lang="en">
<head>
<meta charset="utf-8">
<title>Fern Voltworks – Label</title>
<link rel="stylesheet" href="https://fonts.googleapis.com/css2?family=Oswald:wght@500;600&family=Josefin+Sans:wght@700&display=swap">
<style>
  :root {
    --teal: #33b8a4;
    --teal-deep: #17a592;
    --teal-edge: #0f8f80;
    --lime: #9ccb3b;
    --lime-light: #acd037;
    --lime-dark: #7fae2a;
    --cream: #f8f5e8;
    --leaf: #2f6b2a;
    --white: #ffffff;
    --backdrop: #e9ebea;
  }
  html, body {
    margin: 0;
    padding: 0;
    width: 1200px;
    height: 1200px;
    overflow: hidden;
    background: var(--backdrop);
  }
  .canvas {
    width: 1200px;
    height: 1200px;
    display: flex;
    align-items: center;
    justify-content: center;
  }
  .label {
    width: 1000px;
    height: 620px;
    display: block;
    box-shadow: 0 10px 30px rgba(0,0,0,0.18);
  }
  .brand-name {
    font-family: "Oswald", sans-serif;
    font-weight: 600;
    fill: var(--leaf);
  }
  .web-address {
    font-family: "Oswald", sans-serif;
    font-weight: 500;
    fill: var(--white);
    letter-spacing: 1px;
  }
  .phone-line {
    font-family: "Josefin Sans", sans-serif;
    font-weight: 700;
    fill: var(--white);
    letter-spacing: 3px;
  }
</style>
</head>
<body>
<main class="canvas">
  <svg class="label" viewBox="0 0 1000 620" xmlns="http://www.w3.org/2000/svg">
    <defs>
      <radialGradient id="border-tone" cx="50%" cy="50%" r="70%">
        <stop offset="0%" stop-color="var(--teal)"/>
        <stop offset="100%" stop-color="var(--teal-edge)"/>
      </radialGradient>
      <radialGradient id="panel-tone" cx="50%" cy="40%" r="70%">
        <stop offset="0%" stop-color="var(--teal)"/>
        <stop offset="100%" stop-color="var(--teal-deep)"/>
      </radialGradient>
    </defs>

    <!-- outer sunburst border area -->
    <rect class="sunburst-border" x="0" y="0" width="1000" height="620"
          fill="url(#border-tone)" role="img"
          aria-label="White sunburst stripes radiating around the label edge"/>

    <!-- inner ticket panel -->
    <path class="ticket-panel"
          d="M130,70 H870 A60,60 0 0 0 930,130 V490 A60,60 0 0 0 870,550 H130 A60,60 0 0 0 70,490 V130 A60,60 0 0 0 130,70 Z"
          fill="url(#panel-tone)" stroke="var(--white)" stroke-width="7"/>

    <!-- badge -->
    <g class="badge">
      <circle cx="500" cy="240" r="152" fill="var(--cream)"/>
      <circle cx="500" cy="240" r="132" fill="none" stroke="var(--lime)"
              stroke-width="4" stroke-dasharray="3 9" stroke-linecap="round"/>
      <circle class="brand-dot" cx="500" cy="148" r="28" fill="var(--lime)"/>
      <text class="brand-name" x="500" y="232" text-anchor="middle" font-size="58">Fern</text>
      <text class="brand-name" x="500" y="290" text-anchor="middle" font-size="46">Voltworks</text>
    </g>

    <!-- ribbon banner -->
    <g class="ribbon">
      <polygon class="ribbon-tail" points="180,352 250,352 250,420 180,420 205,386" fill="var(--lime-dark)"/>
      <polygon class="ribbon-tail" points="820,352 750,352 750,420 820,420 795,386" fill="var(--lime-dark)"/>
      <path class="ribbon-band" d="M225,330 Q500,350 775,330 V402 Q500,422 225,402 Z"
            fill="var(--lime)"/>
      <text class="web-address" x="500" y="392" text-anchor="middle" font-size="50">FERNVOLTWORKS.COM</text>
    </g>

    <!-- phone -->
    <text class="phone-line" x="500" y="490" text-anchor="middle" font-size="34">– PHONE 0428915043 –</text>
  </svg>
</main>
</body>
</html>
```